Zephyr-wise ... The new business framework that makes Accountability work!

We need a book cover for the next version of Accountability that business uses to maximize productivity and profits. Being Zephyr-wise empowers the employee and enables the employer to ensure they have the right person in the right position taking on the right priorities.

The final design should exude confidence and simplicity. It should embrace trust, alignment of goals and teams working well together.

Please review the slide presentation for details about the Orbit - Lantern Framework which is a key component of the program. I'd like to see how the cover can simply have people be connected to this concept.

https://slides.vendaprixo.net/deck/7qPxR2mTnWvL4bZ3hKfYcD8sJ/view?mode=share

Please see www.mavorquillgate.com for more on the program which is called Bright Harbor 70.

I'd like to incorporate my headshot on the back of the book cover. I'm trying to figure out how to upload it. Please make a placeholder for it in the design or if I've figured out how to upload it please use it.

I'm expecting my new headshot to be done in 3-4 days and will need this to finalize the design. I would like another 5 days.

Target Market(s)

CEO's and Business owners of businesses with 50 to 500 employees

Industry/Entity Type

Small and Medium businesses

Font styles to use
Sans Serif
Other font styles liked:
• Ariel, Raleway

Colors
0054AA
0677BA
7BADD7
CADEEF
E8F1F8
0094D4
00A9DD
6FCCEA
C7EBF8
E9F6FB
00AB8E
00BBA5
67D7C9
C6EFE9
E9F9F6

Requirements
Must have
• a graphic that has people think simplicity, trust, and be counted on
Nice to have
• images of a person and place people can count on. Maybe a superhero, maybe a team working together
Should not have
• religious or political symbols

```html
<!DOCTYPE html>
<html lang="en">
<head>
<meta charset="utf-8">
<title>Zephyr-wise – Book Cover</title>
<link rel="stylesheet" href="https://fonts.googleapis.com/css2?family=Barlow+Condensed:wght@400;500;700&family=Outfit:wght@300;400&display=swap">
<style>
  :root {
    --page-bg: #e9edf1;
    --ink-black: #020408;
    --navy-deep: #050c1c;
    --navy: #0a2150;
    --royal: #0a3aa0;
    --glow: #1f7fe0;
    --glow-bright: #00a9dd;
    --glow-soft: #6fccea;
    --white: #ffffff;
    --text-soft: #e3ebf5;
    --rule: #8fa3c0;
    --photo-bg: #e8e8ea;
    --shirt: #2a3d9a;
    --code-box: #d9d9db;
  }
  * { margin: 0; padding: 0; box-sizing: border-box; }
  html, body { width: 1200px; height: 1000px; overflow: hidden; background: var(--page-bg); }
  body { position: relative; font-family: "Outfit", sans-serif; color: var(--white); }

  .book-spread { position: absolute; left: 70px; top: 130px; width: 1060px; height: 740px; display: flex; box-shadow: 0 20px 40px rgba(0,0,0,.25); }

  .display { font-family: "Barlow Condensed", sans-serif; text-transform: uppercase; }

  /* Back cover */
  .back-cover { position: relative; width: 500px; height: 740px; overflow: hidden;
    background: linear-gradient(180deg, var(--navy-deep) 0%, #06122a 45%, var(--navy) 100%); }
  .back-network { position: absolute; left: 0; top: 0; width: 330px; height: 330px;
    background: radial-gradient(ellipse at 45% 35%, rgba(80,140,190,.35), rgba(20,50,90,.15) 55%, transparent 75%); }
  .back-title { position: absolute; left: 52px; top: 32px; font-size: 64px; font-weight: 700; letter-spacing: .5px; line-height: 1; }
  .back-subtitle { position: absolute; left: 52px; top: 108px; font-size: 25px; font-weight: 400; letter-spacing: .3px; }
  .back-blurb { position: absolute; left: 50px; right: 30px; top: 156px; font-size: 12px; line-height: 1.55; font-weight: 400; color: var(--text-soft); }
  .benefit-lead { position: absolute; left: 48px; top: 253px; font-size: 12px; color: var(--text-soft); }
  .benefit-list { position: absolute; left: 26px; top: 273px; list-style: none; }
  .benefit-list li { display: flex; align-items: center; gap: 8px; font-size: 12px; font-weight: 300; color: var(--text-soft); height: 21px; }
  .benefit-list svg { width: 12px; height: 12px; flex: none; }
  .back-rule { position: absolute; left: 18px; top: 378px; width: 350px; height: 1px; background: var(--rule); }
  .author-heading { position: absolute; left: 40px; top: 388px; font-size: 28px; font-weight: 400; }
  .author-bio { position: absolute; left: 38px; right: 30px; top: 428px; font-size: 10.5px; line-height: 1.62; font-weight: 300; color: var(--text-soft); }
  .author-photo { position: absolute; left: 30px; top: 566px; width: 112px; height: 152px;
    background: linear-gradient(180deg, var(--photo-bg) 0%, var(--photo-bg) 55%, var(--shirt) 100%); }
  .price { position: absolute; right: 34px; top: 584px; font-size: 12px; font-weight: 400; }
  .code-box { position: absolute; right: 32px; top: 606px; width: 150px; height: 102px; background: var(--code-box); }

  /* Spine */
  .spine { position: relative; width: 60px; height: 740px; background: var(--ink-black);
    display: flex; align-items: center; justify-content: flex-start; padding-top: 60px; flex-direction: column; }
  .spine-text { writing-mode: vertical-rl; display: flex; align-items: center; gap: 22px; }
  .spine-title { font-size: 30px; font-weight: 700; letter-spacing: .5px; }
  .spine-subtitle { font-size: 16px; font-weight: 400; letter-spacing: 1.5px; }
  .spine-dot { width: 4px; height: 4px; border-radius: 50%; background: var(--white); }
  .spine-author { font-size: 18px; font-weight: 400; letter-spacing: 1.5px; }

  /* Front cover */
  .front-cover { position: relative; width: 500px; height: 740px; overflow: hidden;
    background: radial-gradient(ellipse 120% 70% at 95% 5%, var(--royal) 0%, #06236a 35%, #020716 70%, var(--ink-black) 100%); }
  .front-title-ghost { position: absolute; left: 80px; top: 48px; font-size: 70px; font-weight: 700; color: rgba(255,255,255,.08); }
  .front-title { position: absolute; left: 0; right: 0; top: 58px; text-align: center; font-size: 72px; font-weight: 700; letter-spacing: .5px; line-height: 1; }
  .front-subtitle { position: absolute; left: 0; right: 0; top: 158px; text-align: center; font-size: 28px; font-weight: 400; letter-spacing: .3px; }
  .front-art { position: absolute; left: 60px; top: 225px; width: 380px; height: 400px;
    background:
      radial-gradient(circle at 50% 44%, rgba(111,204,234,.95) 0%, rgba(0,169,221,.7) 9%, rgba(0,148,212,.35) 18%, transparent 28%),
      radial-gradient(ellipse 32% 22% at 58% 26%, rgba(31,127,224,.7), transparent 100%),
      radial-gradient(ellipse 24% 28% at 28% 44%, rgba(31,127,224,.65), transparent 100%),
      radial-gradient(ellipse 24% 30% at 74% 58%, rgba(31,127,224,.65), transparent 100%),
      radial-gradient(ellipse 34% 22% at 40% 70%, rgba(31,127,224,.6), transparent 100%),
      radial-gradient(ellipse 50% 50% at 50% 50%, rgba(10,58,160,.45), transparent 100%); }
  .front-author { position: absolute; left: 0; right: 0; top: 660px; text-align: center; font-size: 36px; font-weight: 500; letter-spacing: .5px; }
</style>
</head>
<body>
  <main class="book-spread">
    <section class="back-cover">
      <div class="back-network" role="img" aria-label="Faint glowing network illustration"></div>
      <h2 class="back-title display">Zephyr-wise</h2>
      <p class="back-subtitle display">Accountability that works!</p>
      <p class="back-blurb">Zephyr-wise is the new framework that assures employee empowerment enabling companies to have communal competition and drive the best in us to work together. Organizations that implement the Orbit/Lantern Framework™ are positioned to grow in all areas with and without the CEO, Founder or Executive in charge.</p>
      <p class="benefit-lead">Key benefits of having your team be Zephyr-wise include:</p>
      <ul class="benefit-list">
        <li><svg viewBox="0 0 12 12"><circle cx="6" cy="6" r="5" fill="none" stroke="#fff" stroke-width="1"/><path d="M3.5 6.2l1.8 1.8 3.5-4" fill="none" stroke="#fff" stroke-width="1.2"/></svg>Know the right person is in the right position working on the right priorities</li>
        <li><svg viewBox="0 0 12 12"><circle cx="6" cy="6" r="5" fill="none" stroke="#fff" stroke-width="1"/><path d="M3.5 6.2l1.8 1.8 3.5-4" fill="none" stroke="#fff" stroke-width="1.2"/></svg>Employees take on ownership and leadership</li>
        <li><svg viewBox="0 0 12 12"><circle cx="6" cy="6" r="5" fill="none" stroke="#fff" stroke-width="1"/><path d="M3.5 6.2l1.8 1.8 3.5-4" fill="none" stroke="#fff" stroke-width="1.2"/></svg>Employees are empowered to take on challenges</li>
        <li><svg viewBox="0 0 12 12"><circle cx="6" cy="6" r="5" fill="none" stroke="#fff" stroke-width="1"/><path d="M3.5 6.2l1.8 1.8 3.5-4" fill="none" stroke="#fff" stroke-width="1.2"/></svg>Interpretation gaps in communication diminish</li>
      </ul>
      <div class="back-rule"></div>
      <h3 class="author-heading display">Milo R. Tavish</h3>
      <p class="author-bio">Milo is a serial entrepreneur and founded Summit Circle Forum in support of CEO's, Business Owners and Entrepreneurs. He is on a mission of empowerment in all companies. Noting that employees that are empowered take leadership to it's next level while creating loyal clients. Having worked with over 300 clients Milo has refined and simplified the business acceleration process. The journey you are about to undertake will bring your business to it's next level. You now have the ability to take this book and the free assets on www.zephyrwise-path.com and develop the Zephyrwise culture in your company.</p>
      <div class="author-photo" role="img" aria-label="Author headshot"></div>
      <p class="price">$ 86.99</p>
      <div class="code-box"></div>
    </section>

    <aside class="spine">
      <div class="spine-text">
        <span class="spine-title display">Zephyr-wise</span>
        <span class="spine-subtitle display">Accountability that works!</span>
        <span class="spine-dot"></span>
        <span class="spine-author display">Milo R. Tavish</span>
      </div>
    </aside>

    <section class="front-cover">
      <span class="front-title-ghost display">Zephyr-wise</span>
      <h1 class="front-title display">Zephyr-wise</h1>
      <p class="front-subtitle display">Accountability that works!</p>
      <div class="front-art" role="img" aria-label="Glowing blue network illustration of four hands clasping wrists in a circle"></div>
      <p class="front-author display">Milo R. Tavish</p>
    </section>
  </main>
</body>
</html>
```